Flyer für den Verkauf mediterraner Pflanzen
Zielgruppe
Verkauf winterharter mediterraner Pflanzen
Aufgabenstellung
Die Farben und Schriften sollten von der Homepage übernommen werden um ein einheitliches Design zu erzeugen
Natürlich sind wir jedoch für bessere Ideen gerne zu haben

```html
<!DOCTYPE html>
<html lang="de">
<head>
<meta charset="utf-8">
<title>Verdantio Mediterran – Flyer</title>
<link href="https://fonts.googleapis.com/css2?family=Cabin+Sketch:wght@400;700&family=Red+Hat+Display:wght@400;500;600;700&display=swap" rel="stylesheet">
<style>
:root{
  --stage:#cbcbcb;
  --teal:#5f9e90;
  --teal-soft:#d3e6e3;
  --teal-line:#9fd6cc;
  --forest:#0d4a36;
  --ink-teal:#3f7f70;
  --white:#ffffff;
}
*{box-sizing:border-box;margin:0;padding:0}
html,body{width:1200px;height:1117px;overflow:hidden;background:var(--stage)}
body{position:relative;font-family:"Red Hat Display",sans-serif}
.page{position:absolute;top:174px;width:542px;height:769px;overflow:hidden;background:var(--white)}
.page--front{left:48px}
.page--back{left:610px;background:var(--teal-soft)}
.abs{position:absolute}
.sketch{font-family:"Cabin Sketch",sans-serif;font-weight:700}
.photo{position:absolute}

/* front */
.brand{left:37px;top:20px;display:flex;align-items:center;gap:9px}
.brand__dot{width:59px;height:59px;border-radius:50%;background:var(--teal)}
.brand__name{font-weight:700;font-size:17px;letter-spacing:1px;color:var(--forest);line-height:1.15}
.intro{left:0;top:92px;width:542px;height:251px;background:var(--teal)}
.headline{left:39px;top:112px;font-size:26.5px;line-height:27px;color:var(--teal-soft);letter-spacing:.4px}
.intro-copy{left:39px;top:181px;font-size:8.7px;line-height:10.9px;font-weight:600;color:var(--white);white-space:nowrap}
.intro-copy p+p{margin-top:10.9px}
.themes{left:0;top:343px;width:542px;height:110px;background:var(--teal-soft)}
.theme{position:absolute;top:326px;text-align:center;transform:translateX(-50%);white-space:nowrap}
.theme__icon{width:41px;height:41px;border-radius:50%;background:var(--forest);border:2px solid var(--white);margin:0 auto}
.theme__title{font-family:"Cabin Sketch",sans-serif;font-weight:700;font-size:17px;line-height:18px;color:var(--ink-teal);height:38px;display:flex;align-items:flex-end;justify-content:center;margin-top:3px}
.theme__text{font-size:9.2px;line-height:11px;font-weight:500;color:var(--teal);margin-top:5px}
.range{left:340px;top:470px;list-style:none}
.range li{display:flex;align-items:center;gap:7px;height:22.2px;font-family:"Cabin Sketch",sans-serif;font-weight:700;font-size:13.5px;color:var(--ink-teal);letter-spacing:.4px}
.tick{width:9px;height:9px;flex:none}
.contact{left:308px;top:660px;width:234px;height:109px;background:var(--forest);border-top:9px solid var(--teal)}
.contact__title{position:absolute;left:25px;top:16px;font-size:15.5px;color:var(--teal-line);letter-spacing:.3px}
.contact__row{position:absolute;left:25px;display:flex;align-items:center;gap:9px;font-size:12.5px;font-weight:600;color:var(--white)}
.ico{width:12px;height:12px;flex:none}

/* back */
.back-band{left:0;top:155px;width:542px;height:105px;background:var(--teal)}
.back-title{left:47px;top:172px;font-size:30px;color:var(--teal-soft);letter-spacing:1px}
.back-sub{left:47px;top:211px;font-size:13px;line-height:16.5px;font-weight:600;color:var(--white)}
.invite{left:42px;top:274px;font-size:8.6px;line-height:11px;font-weight:600;color:var(--teal);text-transform:uppercase}
.card{position:absolute;width:110px;height:110px;background:var(--white);border-radius:6px;box-shadow:0 2px 5px rgba(0,0,0,.08)}
.card__img{position:absolute;left:22px;top:10px;width:66px;height:90px;border-radius:8px;background:linear-gradient(180deg,#6e9a6a 0%,#4d7a4f 55%,#3a3a3a 100%)}
.label{position:absolute;width:116px;margin-left:-3px;text-align:center;font-size:9.6px;line-height:10.8px;font-weight:700;color:var(--teal);text-transform:uppercase}
.web-tab{left:140px;top:659px;width:262px;height:24px;border-radius:10px 10px 0 0;background:var(--teal);color:var(--white);font-size:8.6px;font-weight:700;text-align:center;line-height:25px}
.footer{left:0;top:681px;width:542px;height:88px;background:var(--forest);border-top:7px solid var(--teal)}
.footer__title{position:absolute;left:43px;top:14px;font-size:20px;color:var(--teal-soft)}
.footer__name{position:absolute;left:43px;top:37px;font-size:10px;line-height:12.5px;font-weight:700;color:var(--white)}
.footer__col{position:absolute;font-size:10px;line-height:15px;font-weight:500;color:var(--white)}
.footer__line{display:flex;align-items:center;gap:6px}
.footer__line .ico{width:10px;height:10px}
</style>
</head>
<body>

<!-- Vorderseite -->
<section class="page page--front">
  <div class="abs brand">
    <span class="brand__dot"></span>
    <span class="brand__name">VERDANTIO<br>MEDITERRAN</span>
  </div>

  <div class="abs intro"></div>
  <svg class="photo" style="left:0;top:0" width="542" height="320" viewBox="0 0 542 320" role="img" aria-label="Foto: alte Olivenbäume im Schaugarten mit Rasen und blauem Himmel">
    <defs>
      <linearGradient id="olive" x1="0" y1="0" x2="0" y2="1">
        <stop offset="0" stop-color="#3f8fdc"/>
        <stop offset=".45" stop-color="#6f9a55"/>
        <stop offset="1" stop-color="#4f9a34"/>
      </linearGradient>
    </defs>
    <path d="M392 0 L542 0 L542 245 C505 290 440 312 385 308 C320 303 278 258 276 205 C274 150 300 118 335 90 C362 66 378 35 392 0 Z" fill="url(#olive)" stroke="#9fd6cc" stroke-width="4"/>
  </svg>
  <h1 class="abs sketch headline">BEI UNS BIST DU<br>GENAU RICHTIG!</h1>
  <div class="abs intro-copy">
    <p>Wir sind dein Spezialist für Palmen, exotische und<br>winterharte mediterrane Pflanzen. Insbesondere<br>in bester Qualität! Wir freuen uns, dir eine reichhaltige<br>Vielfalt bieten zu können – ein Stück pflanzliche<br>Exklusivität, Qualität und Lebensfreude.</p>
    <p>In unserem eigenen Gewächshaus züchten und<br>vermehren wir unsere Pflanzen. Ältere und größere<br>Exemplare werden auch importiert. Viele dieser<br>außergewöhnlichen Pflanzen kannst du in unserem<br>Schaugarten bestaunen. Profitiere von<br>unserer Erfahrung!</p>
  </div>

  <div class="abs themes"></div>
  <div class="theme" style="left:82px">
    <div class="theme__icon" role="img" aria-label="Symbol Garten"></div>
    <div class="theme__title">GARTEN</div>
    <p class="theme__text">Willst du deinem<br>Garten eine exotische<br>Note verleihen?</p>
  </div>
  <div class="theme" style="left:211px">
    <div class="theme__icon" role="img" aria-label="Symbol Terrasse"></div>
    <div class="theme__title">TERRASSE</div>
    <p class="theme__text">Willst du deine Terrasse in<br>deine ganz persönliche<br>Wohlfühloase verwandeln?</p>
  </div>
  <div class="theme" style="left:351px">
    <div class="theme__icon" role="img" aria-label="Symbol Urlaub"></div>
    <div class="theme__title">URLAUBS-<br>FEELING</div>
    <p class="theme__text">Willst du, dass sich<br>jeder Tag in deinem Garten<br>wie Urlaub anfühlt?</p>
  </div>
  <div class="theme" style="left:472px">
    <div class="theme__icon" role="img" aria-label="Symbol Flair"></div>
    <div class="theme__title">FLAIR</div>
    <p class="theme__text">Willst du dir<br>mediterranes Flair<br>nach Hause holen?</p>
  </div>

  <svg class="photo" style="left:0;top:452px" width="308" height="317" viewBox="0 0 308 317">
    <defs>
      <linearGradient id="greenhouse" x1="0" y1="0" x2="1" y2="1">
        <stop offset="0" stop-color="#b9c7c2"/>
        <stop offset=".5" stop-color="#6d8a6a"/>
        <stop offset="1" stop-color="#3f5c44"/>
      </linearGradient>
      <linearGradient id="alley" x1="0" y1="0" x2="0" y2="1">
        <stop offset="0" stop-color="#6e9fd4"/>
        <stop offset=".4" stop-color="#6b7c55"/>
        <stop offset="1" stop-color="#4a4a3c"/>
      </linearGradient>
    </defs>
    <path d="M0 0 H308 V162 L0 130 Z" fill="url(#greenhouse)" role="img" aria-label="Foto: Gärtner im Gewächshaus zwischen mediterranen Pflanzen"/>
    <path d="M0 142 L308 174 V317 H0 Z" fill="url(#alley)" role="img" aria-label="Foto: Reihen von Palmen und Olivenbäumen in Töpfen"/>
  </svg>

  <ul class="abs range">
    <li><svg class="tick" viewBox="0 0 10 10"><circle cx="5" cy="5" r="5" fill="#5f9e90"/><path d="M2.8 5.2 L4.4 6.7 L7.3 3.6" fill="none" stroke="#fff" stroke-width="1.3"/></svg>PALMEN</li>
    <li><svg class="tick" viewBox="0 0 10 10"><circle cx="5" cy="5" r="5" fill="#5f9e90"/><path d="M2.8 5.2 L4.4 6.7 L7.3 3.6" fill="none" stroke="#fff" stroke-width="1.3"/></svg>OLIVENBÄUME</li>
    <li><svg class="tick" viewBox="0 0 10 10"><circle cx="5" cy="5" r="5" fill="#5f9e90"/><path d="M2.8 5.2 L4.4 6.7 L7.3 3.6" fill="none" stroke="#fff" stroke-width="1.3"/></svg>FEIGENBÄUME</li>
    <li><svg class="tick" viewBox="0 0 10 10"><circle cx="5" cy="5" r="5" fill="#5f9e90"/><path d="M2.8 5.2 L4.4 6.7 L7.3 3.6" fill="none" stroke="#fff" stroke-width="1.3"/></svg>BANANENSTAUDEN</li>
    <li><svg class="tick" viewBox="0 0 10 10"><circle cx="5" cy="5" r="5" fill="#5f9e90"/><path d="M2.8 5.2 L4.4 6.7 L7.3 3.6" fill="none" stroke="#fff" stroke-width="1.3"/></svg>TOSCANA-ZYPRESSEN</li>
    <li><svg class="tick" viewBox="0 0 10 10"><circle cx="5" cy="5" r="5" fill="#5f9e90"/><path d="M2.8 5.2 L4.4 6.7 L7.3 3.6" fill="none" stroke="#fff" stroke-width="1.3"/></svg>PINIEN</li>
    <li><svg class="tick" viewBox="0 0 10 10"><circle cx="5" cy="5" r="5" fill="#5f9e90"/><path d="M2.8 5.2 L4.4 6.7 L7.3 3.6" fill="none" stroke="#fff" stroke-width="1.3"/></svg>SEIDENBÄUME</li>
    <li><svg class="tick" viewBox="0 0 10 10"><circle cx="5" cy="5" r="5" fill="#5f9e90"/><path d="M2.8 5.2 L4.4 6.7 L7.3 3.6" fill="none" stroke="#fff" stroke-width="1.3"/></svg>YUCCAS</li>
  </ul>

  <div class="abs contact">
    <div class="sketch contact__title">WE'RE HAPPY TO HELP!</div>
    <div class="contact__row" style="top:46px">
      <svg class="ico" viewBox="0 0 12 12"><circle cx="6" cy="6" r="6" fill="#9fd6cc"/><path d="M3.6 3.2 C3.4 5.6 5.6 8.4 8.6 8.6 L8.8 7.5 L7.5 6.9 L6.9 7.5 C6 7 5 6 4.6 5.1 L5.2 4.5 L4.6 3.2 Z" fill="#0d4a36"/></svg>
      +43 (0)650 2841937
    </div>
    <div class="contact__row" style="top:70px">
      <svg class="ico" viewBox="0 0 12 12"><circle cx="6" cy="6" r="6" fill="#9fd6cc"/><rect x="3" y="3.8" width="6" height="4.4" fill="none" stroke="#0d4a36" stroke-width=".9"/><path d="M3 3.8 L6 6.3 L9 3.8" fill="none" stroke="#0d4a36" stroke-width=".9"/></svg>
      office@verdantio.at
    </div>
  </div>
</section>

<!-- Rückseite -->
<section class="page page--back">
  <div class="photo" style="left:0;top:0;width:542px;height:155px;background:linear-gradient(180deg,#c9d4cf 0%,#9aa88f 55%,#8a8064 100%)" role="img" aria-label="Foto: Gärtner schiebt eine Schubkarre vor Topfpflanzen im Gewächshaus"></div>
  <div class="abs back-band"></div>
  <svg class="photo" style="left:0;top:0" width="542" height="320" viewBox="0 0 542 320" role="img" aria-label="Foto: Hanfpalmen in Töpfen im Schaugarten vor blühendem Seidenbaum">
    <defs>
      <linearGradient id="palms" x1="0" y1="0" x2="0" y2="1">
        <stop offset="0" stop-color="#5fa0e0"/>
        <stop offset=".4" stop-color="#5f8a4a"/>
        <stop offset="1" stop-color="#3e4a34"/>
      </linearGradient>
    </defs>
    <path d="M392 0 L542 0 L542 245 C505 290 440 312 385 308 C320 303 278 258 276 205 C274 150 300 118 335 90 C362 66 378 35 392 0 Z" fill="url(#palms)" stroke="#9fd6cc" stroke-width="4"/>
  </svg>
  <h2 class="abs sketch back-title">VERDANTIO</h2>
  <p class="abs back-sub">dein Spezialist für Palmen<br>und exotische Pflanzen</p>
  <p class="abs invite">Come by and convince yourself<br>of our diversity. Visit our show garden.<br>Or look in the online shop.<br>We look forward to seeing you!</p>

  <div class="card" style="left:42px;top:334px"><div class="card__img" role="img" aria-label="Produktfoto Agave parryi"></div></div>
  <div class="card" style="left:158px;top:334px"><div class="card__img" role="img" aria-label="Produktfoto Agave victoriae-reginae"></div></div>
  <div class="card" style="left:274px;top:334px"><div class="card__img" role="img" aria-label="Produktfoto Banane Musa basjoo"></div></div>
  <div class="card" style="left:390px;top:334px"><div class="card__img" role="img" aria-label="Produktfoto Baumfarn Dicksonia antarctica"></div></div>
  <div class="label" style="left:42px;top:459px">AGAVE PARRYI</div>
  <div class="label" style="left:158px;top:448px">AGAVE<br>VICTORIAE-<br>REGINAE</div>
  <div class="label" style="left:274px;top:453px">BANANE<br>MUSA BASJOO</div>
  <div class="label" style="left:390px;top:448px">BAUMFARN<br>DICKSONIA<br>ANTARCTICA</div>

  <div class="card" style="left:42px;top:499px"><div class="card__img" role="img" aria-label="Produktfoto Blauglockenbaum Paulownia tomentosa"></div></div>
  <div class="card" style="left:158px;top:499px"><div class="card__img" role="img" aria-label="Produktfoto Chinesische Hanfpalme"></div></div>
  <div class="card" style="left:274px;top:499px"><div class="card__img" role="img" aria-label="Produktfoto Chinesische Hanfpalme mit Stamm"></div></div>
  <div class="card" style="left:390px;top:499px"><div class="card__img" role="img" aria-label="Produktfoto Chilenische Andentanne"></div></div>
  <div class="label" style="left:42px;top:616px">BLAUGLOCKENBAUM<br>PAULOWNIA<br>TOMENTOSA</div>
  <div class="label" style="left:158px;top:616px">CHIN. HANFPALME<br>TRACHYCARPUS<br>FORTUNEI</div>
  <div class="label" style="left:274px;top:616px">CHIN. HANFPALME<br>TRACHYCARPUS<br>FORTUNEI</div>
  <div class="label" style="left:390px;top:616px">CHILENISCHE<br>ANDENTANNE<br>ARAUKARIE</div>

  <div class="abs web-tab">EINZELHEITEN FINDEN SIE AUF UNSERER WEBSITE</div>

  <div class="abs footer">
    <div class="sketch footer__title">BESUCHE UNS!</div>
    <div class="footer__name">Verdantio Mediterran<br>Lukas Brenner</div>
    <div class="footer__col" style="left:197px;top:15px">
      <div class="footer__line">
        <svg class="ico" viewBox="0 0 10 10"><path d="M5 0.5 C2.8 0.5 1.5 2 1.5 3.8 C1.5 6.2 5 9.5 5 9.5 C5 9.5 8.5 6.2 8.5 3.8 C8.5 2 7.2 0.5 5 0.5 Z" fill="#9fd6cc"/><circle cx="5" cy="3.8" r="1.3" fill="#0d4a36"/></svg>
        Lindenweg 27
      </div>
      <div style="padding-left:16px">47°03'18.4"N 15°27'51.6"E<br>A – 8010 Graz</div>
    </div>
    <div class="footer__col" style="left:366px;top:15px">
      <div class="footer__line">
        <svg class="ico" viewBox="0 0 12 12"><circle cx="6" cy="6" r="6" fill="#9fd6cc"/><path d="M3.6 3.2 C3.4 5.6 5.6 8.4 8.6 8.6 L8.8 7.5 L7.5 6.9 L6.9 7.5 C6 7 5 6 4.6 5.1 L5.2 4.5 L4.6 3.2 Z" fill="#0d4a36"/></svg>
        +43 (0)650 2841937
      </div>
      <div class="footer__line">
        <svg class="ico" viewBox="0 0 12 12"><circle cx="6" cy="6" r="6" fill="#9fd6cc"/><rect x="3" y="3.8" width="6" height="4.4" fill="none" stroke="#0d4a36" stroke-width=".9"/><path d="M3 3.8 L6 6.3 L9 3.8" fill="none" stroke="#0d4a36" stroke-width=".9"/></svg>
        office@verdantio.at
      </div>
      <div class="footer__line">
        <svg class="ico" viewBox="0 0 12 12"><circle cx="6" cy="6" r="5.3" fill="none" stroke="#9fd6cc" stroke-width="1.2"/><ellipse cx="6" cy="6" rx="2.2" ry="5.3" fill="none" stroke="#9fd6cc" stroke-width=".9"/><path d="M0.8 6 H11.2" stroke="#9fd6cc" stroke-width=".9"/></svg>
        verdantio.at
      </div>
    </div>
  </div>
</section>

</body>
</html>
```